Business Card Design

I need a business card for my rental business. The business is named:
Hire a Vorlatrike Brenmoor
www.hireavorlatrikebrenmoor.example
(555) 014-2937
This will be a business card that I will leave at other businesses as advertisement so it needs to have the name, website, and phone number.
Please feel free to be creative. This is a new business so I have no designs.
Thank you very much for your time and I look forward to receiving your designs
Target Market(s)
Local rental customers
Industry/Entity Type
Business
Contact Information for Business Card
Please check out my website:
Other font styles liked:
- anything creative
Colors
Designer to choose colors to be used in the design.
Requirements
Must have
- Business name, phone, website. Rentals available hourly or daily. Book online

```html
<!DOCTYPE html>
<html lang="en">
<head>
<meta charset="utf-8">
<title>Hire a Vorlatrike Brenmoor — Business Card</title>
<link rel="stylesheet" href="https://fonts.googleapis.com/css2?family=Oswald:wght@700&family=Exo+2:wght@400;500&display=swap">
<style>
  :root {
    --backdrop: #2b2b2b;
    --card-light: #ffffff;
    --card-dark: #000000;
    --ink-dark: #000000;
    --ink-light: #ffffff;
    --ink-muted: #3a3a3a;
  }
  html, body {
    margin: 0;
    padding: 0;
    width: 1189px;
    height: 1200px;
    overflow: hidden;
    background: var(--backdrop);
  }
  .canvas {
    position: relative;
    width: 1189px;
    height: 1200px;
  }
  .card {
    position: absolute;
    left: 171px;
    width: 857px;
    height: 488px;
    border-radius: 26px;
    box-sizing: border-box;
  }
  .card--front {
    top: 67px;
    background: var(--card-light);
    color: var(--ink-dark);
  }
  .card--back {
    top: 626px;
    background: var(--card-dark);
    color: var(--ink-light);
  }
  .brand-name {
    position: absolute;
    left: 0;
    right: 0;
    margin: 0;
    text-align: center;
    font-family: "Oswald", "Arial Narrow", sans-serif;
    font-weight: 700;
    font-size: 51px;
    line-height: 1;
    letter-spacing: -0.5px;
    text-transform: uppercase;
    white-space: nowrap;
    transform: translateY(-50%);
  }
  .card--front .brand-name { top: 244px; }
  .card--back .brand-name { top: 149px; font-size: 48px; }
  .tagline {
    position: absolute;
    left: 0;
    right: 0;
    top: 318px;
    margin: 0;
    text-align: center;
    font-family: "Exo 2", sans-serif;
    font-weight: 500;
    font-size: 20px;
    line-height: 1;
    letter-spacing: 1.2px;
    color: var(--ink-muted);
    white-space: nowrap;
    transform: translateY(-50%);
  }
  .contact {
    position: absolute;
    left: 0;
    right: 0;
    margin: 0;
    text-align: center;
    font-family: "Exo 2", sans-serif;
    font-weight: 500;
    font-size: 22px;
    line-height: 1;
    letter-spacing: 0.8px;
    white-space: nowrap;
    transform: translateY(-50%);
  }
  .contact--address { top: 268px; }
  .contact--phone { top: 322px; }
  .contact--web { top: 380px; letter-spacing: 1px; }
  .contact--web .web-domain {
    font-size: 22px;
    letter-spacing: 2.4px;
    text-transform: uppercase;
  }
  .contact--web .web-affix {
    font-size: 18px;
    letter-spacing: 1.6px;
  }
</style>
</head>
<body>
  <main class="canvas">
    <section class="card card--front" aria-label="Card front">
      <h1 class="brand-name">Hire a Vorlatrike Brenmoor</h1>
      <p class="tagline">Rentals available hourly or daily · Book online</p>
    </section>

    <section class="card card--back" aria-label="Card back">
      <h2 class="brand-name">Hire a Vorlatrike Brenmoor</h2>
      <p class="contact contact--address">Route 12, Brenmoor, Calden 40917, Westland</p>
      <p class="contact contact--phone">(555) 014-2937</p>
      <p class="contact contact--web"><span class="web-affix">www.</span><span class="web-domain">hireavorlatrikebrenmoor</span><span class="web-affix">.example</span></p>
    </section>
  </main>
</body>
</html>
```